Podcast Marketing Template for LinkedIn

I would like to have graphics to post notices of new podcast episodes on LinkedIn as release new episodes.
The graphics need to be in a template form that can be easily updated by my VA.
Each episode will have a new title and guest.
Two examples of a ROUGH DRAFT of an episode example are attached.
(I do not like these because I think they reflect the standards I have for my brand.)
The posts should be bright and clean and clearly reflect QUALITY of the podcast in the quality of the design. Audience and interviewees are CEOs.
Please refer to my website and podcast art to see brand direction.
www.lorenbriskadvisory.com
Each

```html
<!DOCTYPE html>
<html lang="en">
<head>
<meta charset="utf-8">
<title>Summit Ledger Podcast – Episode Posts</title>
<link rel="stylesheet" href="https://fonts.googleapis.com/css2?family=Bebas+Neue&family=Poppins:ital,wght@0,500;0,700;1,300&display=swap">
<style>
  :root {
    --page: #d6d6d6;
    --brand-blue: #1f5a9c;
    --brand-blue-light: #3474bb;
    --brand-ink: #1d4f8e;
    --white: #ffffff;
    --photo-top: #8d9196;
    --photo-bottom: #1e3f6e;
    --guest-top: #b9d2e8;
    --guest-bottom: #24385a;
  }
  * { box-sizing: border-box; margin: 0; padding: 0; }
  html, body { width: 1034px; height: 1200px; overflow: hidden; }
  body { background: var(--page); position: relative; font-family: "Poppins", sans-serif; }

  .post { position: absolute; background: var(--white); overflow: hidden; box-shadow: 0 14px 24px rgba(0,0,0,.28); }
  .post--square { left: 272px; top: 80px; width: 490px; height: 490px; }
  .post--wide { left: 80px; top: 636px; width: 873px; height: 491px; }

  .post__backdrop { position: absolute; inset: 0; width: 100%; height: 100%; }

  .brand { position: absolute; display: flex; align-items: center; gap: 8px; }
  .brand__mark { width: 54px; height: 54px; background: var(--white); opacity: .85; }
  .brand__name { color: var(--white); font-weight: 700; font-size: 17px; line-height: 17px; }

  .episode-title { position: absolute; font-family: "Bebas Neue", sans-serif; color: var(--white); line-height: .88; letter-spacing: -.5px; }
  .episode-title span { display: block; }

  .host-photo { position: absolute; background: linear-gradient(180deg, var(--photo-top) 0%, #5a6470 35%, var(--photo-bottom) 70%); }
  .guest-photo { position: absolute; border: 3px solid var(--white); border-radius: 18px; background: linear-gradient(180deg, var(--guest-top) 0%, #8aa8c6 45%, var(--guest-bottom) 100%); box-shadow: 0 6px 12px rgba(0,0,0,.25); }

  .guest { position: absolute; color: var(--brand-ink); }
  .guest__with { font-style: italic; font-weight: 300; display: block; }
  .guest__name { font-weight: 700; display: block; letter-spacing: -.5px; }
  .guest__role { font-weight: 500; display: block; }

  .host { position: absolute; color: var(--white); text-align: right; }
  .host__name { font-weight: 700; display: block; letter-spacing: -.5px; }
  .host__role { font-style: italic; font-weight: 300; display: block; }

  /* square post */
  .post--square .brand { left: 33px; top: 24px; }
  .post--square .episode-title { left: 20px; top: 108px; font-size: 44px; }
  .post--square .episode-title .episode-title__lead { font-size: 56px; }
  .post--square .host-photo { left: 265px; top: 16px; width: 212px; height: 451px; border-bottom-left-radius: 190px 170px; }
  .post--square .guest-photo { left: 70px; top: 266px; width: 138px; height: 138px; }
  .post--square .guest { left: 30px; width: 214px; top: 408px; text-align: center; }
  .post--square .guest__with { font-size: 17px; line-height: 20px; }
  .post--square .guest__name { font-size: 21px; line-height: 26px; }
  .post--square .guest__role { font-size: 18px; line-height: 22px; }
  .post--square .host { right: 26px; top: 404px; }
  .post--square .host__name { font-size: 17px; line-height: 21px; }
  .post--square .host__role { font-size: 18px; line-height: 22px; }

  /* wide post */
  .post--wide .brand { left: 77px; top: 16px; }
  .post--wide .episode-title { left: 80px; top: 100px; font-size: 74px; }
  .post--wide .episode-title .episode-title__lead { font-size: 96px; }
  .post--wide .host-photo { left: 519px; top: 16px; width: 320px; height: 451px; border-bottom-left-radius: 300px 220px; }
  .post--wide .guest-photo { left: 68px; top: 330px; width: 137px; height: 137px; }
  .post--wide .guest { left: 232px; top: 380px; }
  .post--wide .guest__with { font-size: 20px; line-height: 22px; }
  .post--wide .guest__name { font-size: 26px; line-height: 30px; }
  .post--wide .guest__role { font-size: 21px; line-height: 25px; }
  .post--wide .host { right: 34px; top: 403px; }
  .post--wide .host__name { font-size: 20px; line-height: 24px; }
  .post--wide .host__role { font-size: 21px; line-height: 25px; }
</style>
</head>
<body>

<section class="post post--square" aria-label="Square episode post">
  <svg class="post__backdrop" viewBox="0 0 490 490" aria-hidden="true">
    <defs>
      <linearGradient id="blueSquare" x1="0" y1="0" x2="1" y2="1">
        <stop offset="0" stop-color="#2766ad"/>
        <stop offset="1" stop-color="#1b5192"/>
      </linearGradient>
    </defs>
    <path d="M0 0 H490 V381 H72 C38 370 12 345 0 310 Z" fill="url(#blueSquare)"/>
  </svg>
  <div class="brand">
    <div class="brand__mark"></div>
    <div class="brand__name">Summit<br>Ledger<br>Podcast</div>
  </div>
  <h1 class="episode-title">
    <span>Technology and</span>
    <span>Philanthropy in</span>
    <span class="episode-title__lead">Education</span>
  </h1>
  <div class="host-photo" role="img" aria-label="Host portrait in navy suit against a black-and-white city skyline"></div>
  <div class="guest-photo" role="img" aria-label="Guest portrait in dark blazer"></div>
  <p class="guest">
    <span class="guest__with">WITH</span>
    <span class="guest__name">MARCUS HALE</span>
    <span class="guest__role">CEO of Norvane</span>
  </p>
  <p class="host">
    <span class="host__name">DANIEL REEVE</span>
    <span class="host__role">HOST</span>
  </p>
</section>

<section class="post post--wide" aria-label="Wide episode post">
  <svg class="post__backdrop" viewBox="0 0 873 491" aria-hidden="true">
    <defs>
      <linearGradient id="blueWide" x1="0" y1="1" x2="1" y2="0">
        <stop offset="0" stop-color="#3474bb"/>
        <stop offset=".45" stop-color="#1f5a9c"/>
        <stop offset="1" stop-color="#1c5394"/>
      </linearGradient>
    </defs>
    <path d="M24 0 H873 V368 H200 C100 368 24 310 24 235 Z" fill="url(#blueWide)"/>
  </svg>
  <div class="brand">
    <div class="brand__mark"></div>
    <div class="brand__name">Summit<br>Ledger<br>Podcast</div>
  </div>
  <h2 class="episode-title">
    <span>Technology and</span>
    <span>Philanthropy in</span>
    <span class="episode-title__lead">Education</span>
  </h2>
  <div class="host-photo" role="img" aria-label="Host portrait in navy suit against a black-and-white city skyline"></div>
  <div class="guest-photo" role="img" aria-label="Guest portrait in dark blazer"></div>
  <p class="guest">
    <span class="guest__with">WITH</span>
    <span class="guest__name">MARCUS HALE</span>
    <span class="guest__role">CEO of Norvane</span>
  </p>
  <p class="host">
    <span class="host__name">DANIEL REEVE</span>
    <span class="host__role">HOST</span>
  </p>
</section>

</body>
</html>
```